Illustration/Web Design Project

We need an illustration that communicates how our system works.
We're building a system that helps people find small service providers through their friends. The way it works is the following:
Say Mark is a math tutor. He comes to our website, creates his profile, and connects his Plimora account. Let's say he has 300 Plimora friends, including Linda.
Later, Ruth needs a math tutor. She's Linda's cousin. When she searches on our site for a math tutor, she would see Mark in search results, along with Linda. This will convey an immediate sense of trust.
We're thinking maybe we could illustrate some type of network overview. Maybe even show a snippet of a search results page (we can provide this). We'd also love it if it could be humanized as much as possible (e.g. somehow convey the above example with people's names).
And we want this all to be conveyed on our homepage without requiring the user to scroll. They should be able to instantly scan it and understand it!

```html
<!DOCTYPE html>
<html lang="en">
<head>
<meta charset="utf-8">
<title>How Nearkin works: Mark and Ruth</title>
<link href="https://fonts.googleapis.com/css2?family=Patrick+Hand&display=swap" rel="stylesheet">
<style>
  :root {
    --paper: #fdfdfc;
    --ink: #141414;
    --ink-soft: #555555;
    --band: #d9d9d9;
    --figure-tone: #bdbdbd;
    --figure-light: #e4e4e4;
  }
  * { box-sizing: border-box; margin: 0; padding: 0; }
  html, body { width: 1200px; height: 840px; overflow: hidden; background: var(--paper); }
  body { position: relative; font-family: "Patrick Hand", cursive; color: var(--ink); }
  .story-lines { position: absolute; inset: 0; width: 1200px; height: 840px; }
  .label { position: absolute; white-space: nowrap; line-height: 1; }
  .caption { font-size: 17px; }
  .note { font-size: 23px; }
  .note-small { font-size: 20px; }
  .persona {
    position: absolute;
    background: linear-gradient(180deg, var(--figure-light), var(--figure-tone));
    border-radius: 6px;
  }
  .brand-name {
    position: absolute; width: 68px; height: 68px; border-radius: 50%;
    border: 2px solid var(--ink); background: var(--paper);
    display: flex; align-items: center; justify-content: center;
    font-size: 15px; line-height: 1;
  }
  .network-name { position: absolute; display: flex; align-items: center; gap: 5px; font-size: 15px; line-height: 1; }
  .network-name .dot { width: 14px; height: 14px; border-radius: 50%; background: var(--ink); }
  .signup-button {
    position: absolute; border: 2px solid var(--ink); border-radius: 6px; background: var(--paper);
    font-size: 17px; line-height: 1; display: flex; align-items: center; justify-content: center;
  }
  .page-title { position: absolute; font-size: 22px; font-weight: 400; letter-spacing: 0.5px; line-height: 1; }
  .result-name { position: absolute; font-size: 17px; line-height: 1; }
  .result-text {
    position: absolute; font-size: 14px; line-height: 1.2; color: var(--ink-soft);
    white-space: nowrap; background: var(--paper); padding: 0 3px; margin-left: -3px;
  }
  .empty-avatar { position: absolute; border: 2px solid var(--ink); background: var(--paper); }
</style>
</head>
<body>

<svg class="story-lines" viewBox="0 0 1200 840" aria-hidden="true">
  <defs>
    <marker id="arrowhead" viewBox="0 0 10 10" refX="8" refY="5" markerWidth="9" markerHeight="9" orient="auto">
      <path d="M0,0 L10,5 L0,10" fill="none" stroke="#141414" stroke-width="1.6"/>
    </marker>
  </defs>
  <g fill="none" stroke="#141414" stroke-width="2">
    <path d="M310 148 L894 146"/>
    <path d="M310 148 L310 342"/>
    <rect x="312" y="192" width="580" height="48" fill="#d9d9d9" stroke="none"/>
    <path d="M312 192 L892 190 M312 240 L892 240"/>
    <path d="M326 264 L892 262"/>
    <path d="M322 274 L322 342 M322 274 L892 274"/>

    <path d="M468 488 L1056 486"/>
    <path d="M468 488 L468 744"/>
    <rect x="470" y="534" width="584" height="42" fill="#d9d9d9" stroke="none"/>
    <path d="M470 534 L1054 532 M470 576 L1054 576"/>
    <path d="M484 606 L1054 604"/>
    <path d="M480 616 L1040 616 L1040 720 M480 616 L480 720"/>
    <path d="M540 696 L1040 696"/>

    <path d="M424 128 L424 232" marker-end="url(#arrowhead)"/>
    <path d="M672 134 L672 190" marker-end="url(#arrowhead)"/>
    <path d="M588 452 L588 580" marker-end="url(#arrowhead)"/>
    <path d="M816 480 L606 718" marker-end="url(#arrowhead)"/>
  </g>
</svg>

<div class="label caption" style="left:50px; top:92px;">Mark is a Math tutor</div>
<div class="persona" style="left:78px; top:144px; width:96px; height:166px;" role="img" aria-label="Sketch of Mark, a math tutor with glasses and a sweater vest"></div>

<div class="label note" style="left:312px; top:86px;">He comes to our site</div>
<div class="label note" style="left:314px; top:108px;">creates his profile</div>
<div class="label note-small" style="left:554px; top:110px;">Connects his Plimora account</div>

<div class="brand-name" style="left:344px; top:156px;">Nearkin</div>
<div class="network-name" style="left:640px; top:208px;"><span class="dot"></span>Plimora</div>
<div class="signup-button" style="left:708px; top:203px; width:102px; height:24px;">Sign Up</div>
<h2 class="page-title" style="left:326px; top:242px;">Math Tutor</h2>
<div class="persona" style="left:334px; top:280px; width:32px; height:46px;" role="img" aria-label="Small profile sketch of Mark"></div>
<div class="result-name" style="left:382px; top:284px;">Mark</div>
<div class="result-text" style="left:382px; top:302px;">Algebra, geometry and calculus help for all ages</div>
<div class="result-text" style="left:382px; top:322px;">Evenings and weekends, near campus</div>

<div class="label caption" style="left:206px; top:430px;">Ruth needs a Math tutor</div>
<div class="persona" style="left:250px; top:474px; width:116px; height:138px;" role="img" aria-label="Sketch of Ruth, a woman with curly hair"></div>

<div class="label note" style="left:466px; top:422px;">She searches here and finds Mark</div>
<div class="label note-small" style="left:624px; top:454px;">sees Linda, her cousin as one of Mark's friend in Plimora</div>

<div class="brand-name" style="left:506px; top:494px;">Nearkin</div>
<div class="network-name" style="left:808px; top:549px;"><span class="dot"></span>Plimora</div>
<div class="signup-button" style="left:878px; top:542px; width:104px; height:26px;">Sign Up</div>
<h2 class="page-title" style="left:486px; top:584px;">Math Tutor</h2>
<div class="empty-avatar" style="left:486px; top:624px; width:48px; height:60px;"></div>
<div class="result-name" style="left:540px; top:628px;">Mark</div>
<div class="result-text" style="left:540px; top:648px;">Algebra, geometry and calculus help for all ages</div>
<div class="result-text" style="left:540px; top:672px;">Evenings and weekends, near campus</div>
<div class="persona" style="left:546px; top:706px; width:42px; height:46px;" role="img" aria-label="Small profile sketch of Linda, Ruth's cousin"></div>

</body>
</html>
```